Summer orchestra weekly camp poster BVPE youth orchestra

We are youth orchestra in Texas holds a summer program called: Bright Bow Seasonal Studio (It's for students ages 8-18 who play already play violin/viola/cello/bass in the North Dallas, Texas Area.

We have 2 posters already from Artmarket designers that we have already been using and now are looking for some new designs. (you can see our other two previously purchased designs on the art market website)

The main difference in our camp is that we meet weekly on Saturday for 2 months June and July (not a week or 2 long camp like most music camps). This makes us a better choice locally because you are playing every week for 2 months out if the summer and less likely to lose skills over the summer vacation months.

Poster size: 11" by 17" but needs to be convertible to 8.5 to 11 size as well AND most importantly be in editable format via either Word or Publisher so we can use it every summer and be able to change dates, cost or location as needed.

All the details are below, but on the poster we would need the website listed: www.marlowridgeyouthensemble.example and tell them to go to that website to apply online beginning April 1st

That's how we get business, they go to our website and apply and pay with coinvault. It also needs to say really big BVPE BRIGHT BOW SEASONAL STUDIO

April 1st is when we being accepting online applications (every year, so don't put a year) Also put: Camp is held on Saturdays in June and July with final concert, last Sunday in July

Also on the poster we need: Our goal is to keep young musicians playing over the summer –so don’t put your instrument away for the summer! Keep in shape by joining us for the Marlow Ridge Youth Ensemble’s summer program – Bright Bow Seasonal Studio! Tuition is $225, which covers June/July Saturday rehearsals and the performance fee for the BKMT Hall concert, last Sunday in July.

I know we can't get all the info below on it, but I put it on so you could better understand what we are doing.

We have a logo already, that we have the rights to - I need something that kids/teens will think is cool looking and music related....we are string instruments only (violin, viola, cello, bass) we also want it to look classy looking, not cheap
I included 2 copies of the logo in different color set

here's all the details from our website:
Bright Bow Seasonal Studio (June and July) - Tuition: $225
Somewhere it should stress that we are not like other camps because we are weekly for two months. (There's a better way to state that but I'm not sure what that is)

Rehearsals on Saturdays June &July with final concert on last Sunday in July @ BKH Hall

Our goal is to keep young musicians playing over the summer –so don’t put your instrument away for the summer! Keep in shape by joining us for the Marlow Ridge Youth Ensemble’s new summer program – Bright Bow Seasonal Studio!

Tuition is $225, which covers June/July Saturday rehearsals and the performance fee for the BKMT Hall concert.

No audition is necessary. Enrollment is limited to the first 50 students in each age category, depending on instrumentation needs, so don’t delay – enrollment online begins April 1st. Siblings will receive a $50 discount, after the first child's regular priced tuition.

Bright Bow I: Students entering grades 6 and below (3:00 – 4:20 P.M. )
Bright Bow II: Students grades entering 7 and 8 (4:30 – 6:00 P.M.)
Bright Bow III: Students entering grades 9-12 (6:15 – 7:45 P.M.)

Summer camp attendance policy is more lenient due to summer vacations. Please notify BVPE of summer absences as soon as your vacation/camp dates are known.
Updates

Here is a link to the previous contest we held on ArtMarket last year.

http://jobs.artmarket.example/job.aspx?id=384619

http://poster.artmarket.example/contest.aspx?id=384619

Also Rehearsals are held at Pemberton Fiddles in Allen, TX

I am working today at a music festival and cannot get on the computer or artmarket website until after 6 or 7 p.m. tonight.  So if you are not getting feedback during the day today, that is why.  I will give feedback to everyone when I get home later tonight.  Thank you all for your work!

Reason: Hi everyone, I judged a music contest all day today and really need some time to look over all the entries. I appreciate everyone's hard work and will make a decision within the next 2 days. I want to be able to provide feedback to everyone and give everyone enough time to submit their best work, so I am extending the deadline by 2 days. I will have to make a decision at the end very quickly as we need to do a huge mail out as soon as the contest is over. Thank you everyone, we really do appreciate everyone's efforts in making our new poster for Bright Seasonal Bow Studio!

Target Market(s)

Parents of string players age 8-18 in North Texas along with students themselves.

Industry/Entity Type

Business

Requirements
Must have
• something showing we are different than the ordinary summer music camp
our QR code which I will email to you if your poster is the winner

```html
<!DOCTYPE html>
<html lang="en">
<head>
<meta charset="utf-8">
<title>Bright Bow Seasonal Studio – BVPE</title>
<link rel="stylesheet" href="https://fonts.googleapis.com/css2?family=Poppins:wght@500;600&family=Questrial&display=swap">
<style>
  :root {
    --frame-pink: #f4d9ec;
    --maroon-deep: #5a0a1e;
    --maroon: #7d1530;
    --maroon-light: #9a2642;
    --title-mint: #d8f6c4;
    --text-white: #ffffff;
    --wood-dark: #5b1a06;
    --wood: #b3400f;
    --wood-light: #e0702a;
  }
  * { margin: 0; padding: 0; box-sizing: border-box; }
  html, body {
    width: 1200px; height: 776px; overflow: hidden;
    background: var(--frame-pink);
  }
  .poster {
    position: relative;
    width: 1200px; height: 776px;
    background: var(--frame-pink);
    font-family: "Questrial", "Century Gothic", sans-serif;
    color: var(--text-white);
  }
  .panel {
    position: absolute;
    left: 10px; top: 10px; right: 10px; bottom: 10px;
    overflow: hidden;
    background:
      radial-gradient(ellipse at 55% 45%, var(--maroon-light) 0%, var(--maroon) 45%, var(--maroon-deep) 100%);
  }
  .cello-art {
    position: absolute;
    left: -20px; top: -30px;
    width: 300px; height: 730px;
    border-radius: 0 160px 140px 0 / 0 260px 200px 0;
    background: linear-gradient(100deg, var(--wood-dark) 0%, var(--wood) 45%, var(--wood-light) 70%, var(--wood) 90%);
  }
  .violin-art {
    position: absolute;
    left: 300px; top: 560px;
    width: 900px; height: 170px;
    border-radius: 90px 20px 20px 90px;
    transform: rotate(8deg);
    transform-origin: left center;
    background: linear-gradient(170deg, var(--wood-light) 0%, var(--wood) 40%, var(--wood-dark) 60%, #1c0a08 75%, #1c0a08 100%);
  }
  .website {
    position: absolute;
    left: 40px; top: 640px;
    transform: rotate(-90deg);
    transform-origin: left top;
    font-size: 30px;
    letter-spacing: 0.5px;
    white-space: nowrap;
  }
  .title {
    position: absolute;
    left: 262px; top: 22px;
    font-family: "Poppins", "Century Gothic", sans-serif;
    font-weight: 600;
    font-size: 55px;
    line-height: 72px;
    color: var(--title-mint);
  }
  .brand {
    position: absolute;
    left: 760px; top: 62px;
    display: flex; align-items: center; gap: 18px;
  }
  .brand-dot {
    width: 60px; height: 60px; border-radius: 50%;
    border: 3px solid var(--text-white);
  }
  .brand-name {
    font-family: "Poppins", sans-serif;
    font-weight: 500;
    font-size: 80px;
    line-height: 1;
    color: var(--text-white);
    letter-spacing: 4px;
  }
  .intro p {
    position: absolute;
    font-size: 16.5px;
    line-height: 22px;
    white-space: nowrap;
  }
  .schedule {
    position: absolute;
    left: 900px; top: 316px;
    width: 270px;
    text-align: center;
    font-size: 21px;
    line-height: 27px;
  }
  .session { margin-bottom: 26px; }
  .session-name, .session-time { font-weight: 700; font-family: "Poppins", sans-serif; font-weight: 600; font-size: 19px; }
  .policy {
    position: absolute;
    left: 76px; top: 696px;
    font-family: "Poppins", sans-serif;
    font-weight: 600;
    font-size: 18.5px;
    line-height: 26px;
    white-space: nowrap;
  }
</style>
</head>
<body>
<div class="poster">
  <div class="panel">
    <div class="cello-art" role="img" aria-label="Photograph of a cello body in warm orange-brown wood"></div>
    <div class="violin-art" role="img" aria-label="Photograph of a violin lying diagonally across the lower edge"></div>

    <p class="website">www.marlowridgeyouthensemble.example</p>

    <h1 class="title">Bright Bow<br>Seasonal Studio</h1>

    <div class="brand">
      <span class="brand-dot"></span>
      <span class="brand-name">BVPE</span>
    </div>

    <div class="intro">
      <p style="left:253px; top:186px;">&nbsp;&nbsp;&nbsp;&nbsp;&nbsp;&nbsp;Our goal is to keep young musicians playing over the summer –so</p>
      <p style="left:206px; top:208px;">don’t put your instrument away for the summer!</p>
      <p style="left:200px; top:230px;">Keep in shape by joining us for the Marlow Ridge Youth Ensemble’s</p>
      <p style="left:198px; top:252px;">summer program – Bright Bow Seasonal Studio!</p>
      <p style="left:203px; top:274px;">Tuition is $225, which covers June/July Saturday rehearsals and the</p>
      <p style="left:216px; top:296px;">performance fee for the BKMT Hall concert, last Sunday in July.</p>
      <p style="left:262px; top:318px;">No audition is necessary. Enrollment is limited to the first 50</p>
      <p style="left:266px; top:340px;">students in each age category, depending on instrumentation</p>
      <p style="left:260px; top:362px;">needs, so don’t delay – enrollment online begins April 1st.</p>
      <p style="left:265px; top:384px;">Siblings will receive a $50 discount, after the first child's regular</p>
      <p style="left:275px; top:406px;">priced tuition.</p>
    </div>

    <div class="schedule">
      <div class="session">
        <div class="session-name">Bright Bow I:</div>
        <div>Students entering<br>grades 6 and below</div>
        <div class="session-time">3:00 – 4:20 P.M.</div>
      </div>
      <div class="session">
        <div class="session-name">Bright Bow II:</div>
        <div>Students grades<br>entering 7 and 8</div>
        <div class="session-time">4:30 – 6:00 P.M.</div>
      </div>
      <div class="session">
        <div class="session-name">Bright Bow III:</div>
        <div>Students entering<br>grades 9-12</div>
        <div class="session-time">6:15 – 7:45 P.M.</div>
      </div>
    </div>

    <p class="policy">Summer camp attendance policy is more lenient due to summer vacations.<br>Please notify BVPE of summer absences as soon as your vacation/camp dates are known.</p>
  </div>
</div>
</body>
</html>
```